Real Estate Entrepreneur needs a business card

I am a real estate entrepreneur, I buy houses for investment purposes, I act as a real estate agent representing buyers and sellers in residential home transactions, I am a contractor that does a wide range of home repairs and construction. I'd like a design that can stick with me through the years as my business grows and morphs to fit any niche I decide to pursue as markets change.

Target Market(s)

Anyone with interest that may be related to real estate.

Industry/Entity Type

Real Estate

Contact Information for Business Card

A card that stands out and doesn't put me in any one box. My business will evolve over time and I need a card that can stay relevant.

Colors

Designer to choose colors to be used in the design.

Requirements
Must have
• Character
Nice to have
• I'm open
Should not have
• Cliche houses and hammers

```html
<!DOCTYPE html>
<html lang="en">
<head>
<meta charset="utf-8">
<title>Vance Holt – Business Card</title>
<link href="https://fonts.googleapis.com/css2?family=Michroma&family=Open+Sans:wght@400;600&display=swap" rel="stylesheet">
<style>
  :root {
    --page: #e9e8e6;
    --paper: #ffffff;
    --ink: #1d1d1d;
    --ink-soft: #555555;
    --rule: #c8c8c8;
    --night: #1a1a1a;
    --night-edge: #2a2a2a;
    --on-night: #f2f2f2;
  }
  * { box-sizing: border-box; margin: 0; padding: 0; }
  html, body { width: 1200px; height: 1200px; overflow: hidden; }
  body {
    background: var(--page);
    font-family: "Open Sans", Arial, sans-serif;
    position: relative;
  }
  .card {
    position: absolute;
    left: 180px;
    width: 840px;
    height: 480px;
    box-shadow: 0 6px 18px rgba(0,0,0,0.12);
  }
  .card--front { top: 80px; background: var(--paper); color: var(--ink); }
  .card--back {
    top: 640px;
    background: linear-gradient(135deg, #0f0f0f 0%, var(--night) 50%, var(--night-edge) 100%);
    color: var(--on-night);
  }
  .frame {
    position: absolute;
    inset: 44px 48px;
    border: 2px solid currentColor;
  }
  .card--back .frame { border-color: var(--on-night); }

  /* front */
  .mark {
    position: absolute;
    top: -40px;
    left: 50%;
    transform: translateX(-50%);
    padding: 0 26px;
    background: var(--paper);
  }
  .mark__square { display: block; width: 76px; height: 76px; background: #3a3435; }
  .front-content {
    position: absolute;
    top: 70px;
    left: 0; right: 0;
    text-align: center;
  }
  .name {
    font-family: "Michroma", "Arial Black", sans-serif;
    letter-spacing: 3px;
  }
  .card--front .name { font-size: 40px; }
  .tagline { font-size: 17px; letter-spacing: 1px; color: var(--ink-soft); margin-top: 6px; }
  .divider { width: 110px; height: 1px; background: var(--rule); margin: 18px auto 16px; }
  .details { font-size: 16px; line-height: 1.75; color: var(--ink-soft); letter-spacing: 0.5px; }
  .web {
    position: absolute;
    bottom: -13px;
    left: 50%;
    transform: translateX(-50%);
    padding: 0 22px;
    font-size: 18px;
    font-weight: 600;
    letter-spacing: 2px;
    white-space: nowrap;
  }
  .card--front .web { background: var(--paper); color: var(--ink); }

  /* back */
  .back-content {
    position: absolute;
    top: 118px;
    left: 0; right: 0;
    text-align: center;
  }
  .card--back .name { font-size: 54px; letter-spacing: 4px; }
  .card--back .tagline {
    color: var(--on-night);
    font-size: 19px;
    text-align: right;
    padding-right: 120px;
    margin-top: 4px;
  }
  .card--back .web {
    font-weight: 400;
    font-size: 16px;
    color: var(--on-night);
    background: #181818;
  }
</style>
</head>
<body>
  <section class="card card--front" aria-label="Card front">
    <div class="frame">
      <div class="mark"><span class="mark__square"></span></div>
      <div class="front-content">
        <h1 class="name">VANCE HOLT</h1>
        <p class="tagline">Real Estate Entrepreneur</p>
        <div class="divider"></div>
        <p class="details">Dummy city, Dummy Country Land<br>1-555-010-2040 | vance@holtestates.com</p>
      </div>
      <p class="web">www.holtestates.com</p>
    </div>
  </section>

  <section class="card card--back" aria-label="Card back">
    <div class="frame">
      <div class="back-content">
        <h2 class="name">VANCE HOLT</h2>
        <p class="tagline">Real Estate Entrepreneur</p>
      </div>
      <p class="web">www.holtestates.com</p>
    </div>
  </section>
</body>
</html>
```